New residential property management company

I have a lot of name recognition in our smaller town due to owning a construction company here. I have now started a residential property management company representing landlords and tenants. Just trying to get my name out there and get some rentals to manage!

```html
<!DOCTYPE html>
<html lang="en">
<head>
<meta charset="utf-8">
<title>Harlow Property Management – Flyer</title>
<link rel="stylesheet" href="https://fonts.googleapis.com/css2?family=Heebo:wght@300;400;500;700;800&display=swap">
<style>
  :root{
    --stage:#848484;
    --paper:#ffffff;
    --ink:#1e1e22;
    --band:#222226;
    --photo-light:#2c3a52;
    --photo-mid:#18212f;
    --photo-dark:#0a0e16;
    --portrait-a:#7a6a5c;
    --portrait-b:#3a3230;
    --white:#ffffff;
  }
  html,body{margin:0;padding:0;width:1200px;height:900px;overflow:hidden;background:var(--stage);}
  body{font-family:"Heebo",Arial,sans-serif;color:var(--ink);}
  .flyer{position:absolute;left:60px;top:90px;width:960px;height:640px;transform:scale(1.125);transform-origin:0 0;background:var(--paper);overflow:hidden;box-shadow:0 6px 18px rgba(0,0,0,.25);}
  .hero-photo{position:absolute;inset:0;clip-path:polygon(522px 0,960px 0,960px 640px,418px 640px);
    background:radial-gradient(ellipse 45% 55% at 72% 45%,var(--photo-light),var(--photo-mid) 60%,var(--photo-dark));}
  .divider{position:absolute;inset:0;background:var(--band);clip-path:polygon(508px 0,516px 0,412px 640px,404px 640px);}
  .headline-band{position:absolute;inset:0;background:var(--band);clip-path:polygon(0 127px,479px 127px,462px 235px,0 235px);}
  .contact-band{position:absolute;inset:0;background:var(--band);clip-path:polygon(0 568px,408px 568px,397px 640px,0 640px);}
  .brand{position:absolute;left:36px;top:36px;display:flex;align-items:center;gap:18px;}
  .brand-mark{width:56px;height:56px;background:var(--ink);}
  .brand-name{font-weight:300;font-size:60px;line-height:1;letter-spacing:1px;color:var(--ink);}
  .brand-sub{position:absolute;left:136px;top:100px;font-weight:500;font-size:8.5px;letter-spacing:2.6px;color:var(--ink);text-transform:uppercase;}
  .headline{position:absolute;left:38px;top:138px;margin:0;color:var(--white);font-weight:800;font-size:33px;line-height:47px;letter-spacing:.3px;text-transform:uppercase;}
  .intro{position:absolute;left:38px;top:248px;width:400px;margin:0;font-size:13.8px;line-height:18.8px;text-align:justify;}
  .services-title{position:absolute;left:38px;top:360px;margin:0;font-weight:800;font-size:18.5px;text-transform:uppercase;}
  .services{position:absolute;left:40px;top:388px;margin:0;padding:0;list-style:none;font-size:13.2px;line-height:17.5px;}
  .services li{display:flex;gap:7px;margin-bottom:6px;}
  .services svg{flex:none;width:11px;height:11px;margin-top:3.5px;}
  .cta{position:absolute;left:36px;top:538px;margin:0;font-weight:700;font-size:15.5px;text-transform:uppercase;}
  .contacts{position:absolute;left:38px;top:574px;margin:0;padding:0;list-style:none;color:var(--white);font-size:14px;line-height:25px;}
  .contacts li{display:flex;align-items:center;gap:7px;}
  .contacts svg{width:17px;height:17px;}
  .portrait{position:absolute;left:312px;top:413px;width:216px;height:216px;border-radius:50%;background:var(--band);}
  .portrait-ring{position:absolute;inset:6px;border-radius:50%;background:var(--white);}
  .portrait-fill{position:absolute;inset:12px;border-radius:50%;background:radial-gradient(circle at 50% 40%,var(--portrait-a),var(--portrait-b));}
</style>
</head>
<body>
<main class="flyer">
  <div class="hero-photo" role="img" aria-label="Photo of a businessman in a dark suit holding cupped hands beneath a glowing house outline"></div>
  <div class="divider"></div>
  <div class="headline-band"></div>
  <div class="contact-band"></div>

  <div class="brand">
    <span class="brand-mark"></span>
    <span class="brand-name">HARLOW</span>
  </div>
  <div class="brand-sub">Property Management LLC.</div>

  <h1 class="headline">Get some rentals<br>to manage!</h1>

  <p class="intro">We are a local residential property management company backed by years of experience in building and maintaining homes. We represent both landlords and tenants. Our goal is to help owners ease their work load so they can enjoy the rewards of their rentals without the daily hassle.</p>

  <h2 class="services-title">Our services</h2>
  <ul class="services">
    <li><svg viewBox="0 0 12 12"><circle cx="6" cy="6" r="6" fill="var(--ink)"/><path d="M3.2 6.2l1.9 1.9 3.7-3.9" stroke="#fff" stroke-width="1.5" fill="none"/></svg>Tenant screening, leasing and move-ins</li>
    <li><svg viewBox="0 0 12 12"><circle cx="6" cy="6" r="6" fill="var(--ink)"/><path d="M3.2 6.2l1.9 1.9 3.7-3.9" stroke="#fff" stroke-width="1.5" fill="none"/></svg>Rent collection and monthly owner statements</li>
    <li><svg viewBox="0 0 12 12"><circle cx="6" cy="6" r="6" fill="var(--ink)"/><path d="M3.2 6.2l1.9 1.9 3.7-3.9" stroke="#fff" stroke-width="1.5" fill="none"/></svg><span>Maintenance and repair coordination<br>with trusted local contractors</span></li>
    <li><svg viewBox="0 0 12 12"><circle cx="6" cy="6" r="6" fill="var(--ink)"/><path d="M3.2 6.2l1.9 1.9 3.7-3.9" stroke="#fff" stroke-width="1.5" fill="none"/></svg>Regular property inspections</li>
    <li><svg viewBox="0 0 12 12"><circle cx="6" cy="6" r="6" fill="var(--ink)"/><path d="M3.2 6.2l1.9 1.9 3.7-3.9" stroke="#fff" stroke-width="1.5" fill="none"/></svg>Need something else? Just ask!</li>
  </ul>

  <p class="cta">For free consultation call:</p>
  <ul class="contacts">
    <li><svg viewBox="0 0 18 18"><circle cx="9" cy="9" r="9" fill="#fff"/><path d="M6 4.5l1.6 2.4-1 1.1c.6 1.3 1.5 2.2 2.8 2.8l1.1-1 2.4 1.6-.8 1.6c-3.8-.3-6.6-3.1-6.9-6.9z" fill="var(--band)"/></svg>555-210-3870</li>
    <li><svg viewBox="0 0 18 18"><circle cx="9" cy="9" r="9" fill="#fff"/><rect x="4.5" y="6" width="9" height="6.5" rx="1" fill="var(--band)"/><path d="M4.8 6.4L9 9.5l4.2-3.1" stroke="#fff" stroke-width="1" fill="none"/></svg>harlowpropertymgmt@mailbox.com</li>
  </ul>

  <div class="portrait">
    <div class="portrait-ring"></div>
    <div class="portrait-fill" role="img" aria-label="Portrait photo of the company owner"></div>
  </div>
</main>
</body>
</html>
```